Vordaline - Fitness Coach. Needs a Business Card Design that I can also use for other advertising

Established 2012, I have finished the KTRB National Certificate in Fitness & Personal Training. Harlow Cross First Aid Certificate. I have the Auckland 800m track records for MW45. I also came 1st at the 2012 Pellamar Games in 800 & 1500m. I am passionate about health & fitness and would like to help people reach their health & fitness goals. I also take health & fitness weekends. Main interests - Running, Weight Training, Yoga & Aqua Jogging. I like strength/power, but am femine.

Target Market(s)

Male or Female 18 and over that wants to improve their health & fitness

Industry/Entity Type

Advertising

Requirements
Must have
• my name: Rosalind K Tarbury contact details: ros@quillsend.co.nz mobile - 021 583917 URL name: facebook.com/rosalindKtarbury - VordaLine
Photo of Me

```html
<!DOCTYPE html>
<html lang="en">
<head>
<meta charset="utf-8">
<title>VordaLine – Business Card</title>
<link rel="stylesheet" href="https://fonts.googleapis.com/css2?family=Quicksand:wght@300;400&display=swap">
<style>
  :root {
    --stage: #161616;
    --card-dark: #000000;
    --card-brown: #3a302a;
    --card-orange: #f27c1e;
    --ink-light: #ffffff;
    --photo-warm: #e8731c;
    --photo-shade: #2a2a30;
  }
  * { margin: 0; padding: 0; box-sizing: border-box; }
  html, body {
    width: 1200px;
    height: 900px;
    overflow: hidden;
    background: var(--stage);
  }
  .stage {
    width: 1200px;
    height: 900px;
    display: flex;
    align-items: center;
    justify-content: center;
  }
  .business-card {
    position: relative;
    width: 600px;
    height: 600px;
    overflow: hidden;
    box-shadow: 0 20px 50px rgba(0,0,0,0.6);
  }
  .card-top {
    position: absolute;
    inset: 0 0 auto 0;
    height: 300px;
    background: linear-gradient(200deg, var(--card-brown) 0%, var(--card-dark) 55%);
  }
  .card-bottom {
    position: absolute;
    inset: 300px 0 0 0;
    background: var(--card-orange);
  }
  .coach-photo {
    position: absolute;
    left: 150px;
    top: 40px;
    width: 250px;
    height: 330px;
    border-radius: 40% 40% 30% 30%;
    background: radial-gradient(ellipse at 45% 40%, var(--photo-warm) 0%, rgba(232,115,28,0.55) 35%, var(--photo-shade) 70%, rgba(42,42,48,0) 100%);
  }
  .contact {
    position: absolute;
    left: 110px;
    top: 395px;
    color: var(--ink-light);
    font-family: 'Quicksand', sans-serif;
    font-weight: 300;
  }
  .contact-name {
    font-size: 38px;
    margin-left: 40px;
    margin-bottom: 22px;
    letter-spacing: 0.5px;
  }
  .contact-line {
    font-size: 25px;
    line-height: 1.2;
  }
</style>
</head>
<body>
  <main class="stage">
    <article class="business-card">
      <div class="card-top"></div>
      <div class="card-bottom"></div>
      <div class="coach-photo" role="img" aria-label="Photo of the fitness coach leaping in the air, wearing an orange top and dark leggings"></div>
      <div class="contact">
        <p class="contact-name">Rosalind K. Tarbury</p>
        <p class="contact-line">ros@quillsend.co.nz</p>
        <p class="contact-line">mob.: 021 583917</p>
        <p class="contact-line">facebook - VordaLine</p>
      </div>
    </article>
  </main>
</body>
</html>
```